body balm label design

body balm tube design, current label design for other similar products
Need to have a design which can interchange between 3 different solutions
Quiet Orchard (Lavender + Vanilla)
Copper Trail (Eucalyptus + Mint)
Fern Hollow (Bergamot + Cedarwood)
Tube size:
2.5h x 3.25 w
Target Market(s)
natural, solution focused
Requirements
Must have
- relatable to existing brand designs, focus on features and benefits

```html
<!DOCTYPE html>
<html lang="en">
<head>
<meta charset="utf-8">
<title>Body Balm Labels</title>
<link rel="stylesheet" href="https://fonts.googleapis.com/css2?family=Allura&family=Bodoni+Moda:wght@400;500&family=Montserrat:wght@300;400;600&display=swap">
<style>
  :root {
    --page: #eef0f4;
    --paper: #ffffff;
    --slate: #8a9ca6;
    --teal: #62c7d6;
    --sage: #76a464;
    --copy: #a3abb0;
  }
  html, body { margin: 0; padding: 0; overflow: hidden; }
  body {
    width: 1059px; height: 1200px;
    background: var(--page);
    display: flex; flex-direction: column; align-items: center; justify-content: center;
    gap: 30px;
  }
  .label { width: 468px; height: 360px; display: block; background: var(--paper); }
  .label--orchard { --accent: var(--slate); }
  .label--hollow { --accent: var(--teal); }
  .label--trail { --accent: var(--sage); }

  .artwork { fill: var(--accent); opacity: 0.12; }
  .rule, .band, .badge-mark, .social { fill: var(--accent); }
  .badge-ring { fill: none; stroke: var(--accent); stroke-width: 1.2; }
  .hero-word { font-family: "Bodoni Moda", serif; font-weight: 500; font-size: 60px; fill: var(--accent); }
  .hero-script, .scent { font-family: "Allura", cursive; fill: var(--accent); }
  .hero-script { font-size: 24px; }
  .scent { font-size: 40px; }
  .product-name { font-family: "Montserrat", sans-serif; font-weight: 300; font-size: 25px; fill: #fff; letter-spacing: 0.5px; }
  .brand-inband { font-family: "Montserrat", sans-serif; font-weight: 400; font-size: 8px; fill: #fff; letter-spacing: 1px; }
  .info-head { font-family: "Montserrat", sans-serif; font-weight: 600; font-size: 8px; fill: var(--copy); letter-spacing: 0.6px; }
  .info-body { font-family: "Montserrat", sans-serif; font-weight: 400; font-size: 8px; fill: var(--copy); letter-spacing: 0.5px; }
  .label--hollow .info-head, .label--hollow .info-body { fill: var(--teal); }
  .maker { font-family: "Montserrat", sans-serif; font-size: 8px; fill: var(--copy); letter-spacing: 0.6px; }
  .maker-url { font-family: "Montserrat", sans-serif; font-weight: 600; font-size: 7px; fill: var(--accent); letter-spacing: 1px; }
  .net-weight { font-family: "Montserrat", sans-serif; font-weight: 300; font-size: 12px; fill: var(--accent); }
</style>
</head>
<body>

<!-- Quiet Orchard -->
<svg class="label label--orchard" viewBox="0 0 538 414" xmlns="http://www.w3.org/2000/svg">
  <rect class="artwork" x="14" y="20" width="204" height="370" rx="40" role="img" aria-label="Fine line botanical drawing of lavender and vanilla blossoms"/>
  <rect class="rule" x="220" y="122" width="2" height="292"/>
  <text class="hero-word" transform="translate(196,294) rotate(-90)" textLength="264" lengthAdjust="spacingAndGlyphs">ORCHARD</text>
  <text class="hero-script" transform="translate(222,112) rotate(-90)">quiet</text>
  <path class="band" d="M240 414 V68 A42 42 0 0 1 324 68 V414 Z"/>
  <circle class="badge-mark" cx="282" cy="46" r="3"/>
  <text class="brand-inband" transform="translate(288,130) rotate(-90)">WILLOW FIELD</text>
  <text class="product-name" transform="translate(268,324) rotate(-90)">NATURAL</text>
  <text class="product-name" transform="translate(302,324) rotate(-90)">BODY BALM</text>
  <text class="scent" transform="translate(372,294) rotate(-90)" textLength="262" lengthAdjust="spacingAndGlyphs">Lavender + Vanilla</text>
  <g transform="translate(428,0)">
    <text class="info-head" y="77">Ingredients:</text>
    <text class="info-body"><tspan x="0" y="92">Shea butter,</tspan><tspan x="0" y="103">cocoa butter,</tspan><tspan x="0" y="114">coconut oil,</tspan><tspan x="0" y="125">sweet almond oil,</tspan><tspan x="0" y="136">beeswax,</tspan><tspan x="0" y="147">lavender</tspan><tspan x="0" y="158">essential oil,</tspan><tspan x="0" y="169">vanilla extract or</tspan><tspan x="0" y="180">vanilla oleoresin,</tspan><tspan x="0" y="191">vitamin E oil</tspan></text>
    <text class="info-head" y="212">How to use:</text>
    <text class="info-body"><tspan x="0" y="225">Gently push the</tspan><tspan x="0" y="236">balm up from the</tspan><tspan x="0" y="247">bottom of the</tspan><tspan x="0" y="258">tube using your</tspan><tspan x="0" y="269">finger, apply it</tspan><tspan x="0" y="280">directly to your</tspan><tspan x="0" y="291">skin.</tspan></text>
  </g>
  <circle class="social" cx="438" cy="344" r="8"/><circle class="social" cx="463" cy="344" r="8"/><circle class="social" cx="488" cy="344" r="8"/>
  <text class="maker" x="461" y="371" text-anchor="middle">Made by Willow Field</text>
  <text class="maker-url" x="461" y="384" text-anchor="middle">WWW.WILLOWFIELD.CA</text>
  <circle class="badge-ring" cx="68" cy="300" r="27"/>
  <text class="net-weight" x="40" y="377">NET WT 4 oz</text>
  <text class="net-weight" x="40" y="394">/120g</text>
</svg>

<!-- Fern Hollow -->
<svg class="label label--hollow" viewBox="0 0 538 414" xmlns="http://www.w3.org/2000/svg">
  <rect class="artwork" x="14" y="30" width="204" height="360" rx="40" role="img" aria-label="Fine line botanical drawing of bergamot blossom and fruit"/>
  <rect class="rule" x="220" y="122" width="2" height="292"/>
  <text class="hero-word" transform="translate(196,240) rotate(-90)" textLength="200" lengthAdjust="spacingAndGlyphs">HOLLOW</text>
  <text class="hero-script" transform="translate(222,112) rotate(-90)">fern</text>
  <path class="band" d="M240 414 V68 A42 42 0 0 1 324 68 V414 Z"/>
  <circle class="badge-mark" cx="282" cy="46" r="3"/>
  <text class="brand-inband" transform="translate(288,130) rotate(-90)">WILLOW FIELD</text>
  <text class="product-name" transform="translate(268,324) rotate(-90)">NATURAL</text>
  <text class="product-name" transform="translate(302,324) rotate(-90)">BODY BALM</text>
  <text class="scent" transform="translate(372,368) rotate(-90)" textLength="320" lengthAdjust="spacingAndGlyphs">Bergamot + Cedarwood</text>
  <g transform="translate(428,0)">
    <text class="info-head" y="77">Ingredients:</text>
    <text class="info-body"><tspan x="0" y="92">Shea butter,</tspan><tspan x="0" y="103">cocoa butter,</tspan><tspan x="0" y="114">coconut oil,</tspan><tspan x="0" y="125">sweet almond oil,</tspan><tspan x="0" y="136">beeswax,</tspan><tspan x="0" y="147">lavender</tspan><tspan x="0" y="158">essential oil,</tspan><tspan x="0" y="169">vanilla extract or</tspan><tspan x="0" y="180">vanilla oleoresin,</tspan><tspan x="0" y="191">vitamin E oil</tspan></text>
    <text class="info-head" y="212">How to use:</text>
    <text class="info-body"><tspan x="0" y="225">Gently push the</tspan><tspan x="0" y="236">balm up from the</tspan><tspan x="0" y="247">bottom of the</tspan><tspan x="0" y="258">tube using your</tspan><tspan x="0" y="269">finger, apply it</tspan><tspan x="0" y="280">directly to your</tspan><tspan x="0" y="291">skin.</tspan></text>
  </g>
  <circle class="social" cx="438" cy="344" r="8"/><circle class="social" cx="463" cy="344" r="8"/><circle class="social" cx="488" cy="344" r="8"/>
  <text class="maker" x="461" y="371" text-anchor="middle">Made by Willow Field</text>
  <text class="maker-url" x="461" y="384" text-anchor="middle">WWW.WILLOWFIELD.CA</text>
  <circle class="badge-ring" cx="68" cy="300" r="27"/>
  <text class="net-weight" x="40" y="377">NET WT 4 oz</text>
  <text class="net-weight" x="40" y="394">/120g</text>
</svg>

<!-- Copper Trail -->
<svg class="label label--trail" viewBox="0 0 538 414" xmlns="http://www.w3.org/2000/svg">
  <rect class="artwork" x="60" y="16" width="170" height="380" rx="40" role="img" aria-label="Fine line botanical drawing of eucalyptus and mint leaves"/>
  <rect class="rule" x="220" y="122" width="2" height="292"/>
  <text class="hero-word" transform="translate(196,326) rotate(-90)" textLength="296" lengthAdjust="spacingAndGlyphs">TRAIL</text>
  <text class="hero-script" transform="translate(222,118) rotate(-90)">copper</text>
  <path class="band" d="M240 414 V68 A42 42 0 0 1 324 68 V414 Z"/>
  <circle class="badge-mark" cx="282" cy="46" r="3"/>
  <text class="brand-inband" transform="translate(288,130) rotate(-90)">WILLOW FIELD</text>
  <text class="product-name" transform="translate(268,324) rotate(-90)">NATURAL</text>
  <text class="product-name" transform="translate(302,324) rotate(-90)">BODY BALM</text>
  <text class="scent" transform="translate(372,324) rotate(-90)" textLength="292" lengthAdjust="spacingAndGlyphs">Eucalyptus + Mint</text>
  <g transform="translate(428,0)">
    <text class="info-head" y="77">Ingredients:</text>
    <text class="info-body"><tspan x="0" y="92">Shea butter,</tspan><tspan x="0" y="103">cocoa butter,</tspan><tspan x="0" y="114">coconut oil,</tspan><tspan x="0" y="125">sweet almond oil,</tspan><tspan x="0" y="136">beeswax,</tspan><tspan x="0" y="147">lavender</tspan><tspan x="0" y="158">essential oil,</tspan><tspan x="0" y="169">vanilla extract or</tspan><tspan x="0" y="180">vanilla oleoresin,</tspan><tspan x="0" y="191">vitamin E oil</tspan></text>
    <text class="info-head" y="212">How to use:</text>
    <text class="info-body"><tspan x="0" y="225">Gently push the</tspan><tspan x="0" y="236">balm up from the</tspan><tspan x="0" y="247">bottom of the</tspan><tspan x="0" y="258">tube using your</tspan><tspan x="0" y="269">finger, apply it</tspan><tspan x="0" y="280">directly to your</tspan><tspan x="0" y="291">skin.</tspan></text>
  </g>
  <circle class="social" cx="438" cy="344" r="8"/><circle class="social" cx="463" cy="344" r="8"/><circle class="social" cx="488" cy="344" r="8"/>
  <text class="maker" x="461" y="371" text-anchor="middle">Made by Willow Field</text>
  <text class="maker-url" x="461" y="384" text-anchor="middle">WWW.WILLOWFIELD.CA</text>
  <circle class="badge-ring" cx="68" cy="300" r="27"/>
  <text class="net-weight" x="40" y="377">NET WT 4 oz</text>
  <text class="net-weight" x="40" y="394">/120g</text>
</svg>

</body>
</html>
```